BRAVEN POWERLINE SERVICES needs a vibrant design for electrical contracting work.

I require a card design for my own electrical contracting business. I will be doing a lot of domestic and commercial work, including things such as repairs, maintenance, lighting, installations and various others. LED lighting and energy efficiency will be a big part of my business. I wish not to have childish pictures such as light bulbs in the design, but rather a smart and modern looking card which incorporates my logo colours and perhaps the same lighting strike within the faded background of the card.

Target Market(s)

Residential and Commercial property owners.

Industry/Entity Type

Electrical

Contact Information for Business Card

Dalen Voskic
EC40923
Phone Number: 0417 358 942
Email: dalen@bravenpowerline.com

Font styles to use
Serif
Sans Serif

Requirements
Must have
• My Logo and associated colours.
Nice to have
• Some form of shapes splitting the card into different colours related to the colours of my logo. Electric Blue, Silver/Grey and White.
Should not have
• Childish pictures and symbols such as light bulbs.

```html
<!DOCTYPE html>
<html lang="en">
<head>
<meta charset="utf-8">
<title>Braven Powerline Services – Business Card</title>
<link href="https://fonts.googleapis.com/css2?family=PT+Sans:wght@400;700&family=PT+Serif:wght@400&display=swap" rel="stylesheet">
<style>
  :root {
    --electric-blue: #3a52a4;
    --steel-grey: #6d6e70;
    --card-white: #ffffff;
    --text-light: #ffffff;
    --text-shadow: rgba(10, 20, 60, 0.75);
  }
  html, body {
    margin: 0;
    padding: 0;
    overflow: hidden;
    background: #ffffff;
  }
  .card {
    position: relative;
    width: 702px;
    height: 1200px;
    overflow: hidden;
    background: var(--electric-blue);
    font-family: "PT Sans", Arial, sans-serif;
  }
  .band { position: absolute; left: 0; width: 100%; }
  .band--top { top: 0; height: 119px; background: var(--electric-blue); }
  .band--grey-upper { top: 119px; height: 18px; background: var(--steel-grey); }
  .band--brand { top: 137px; height: 447px; background: var(--card-white); }
  .band--grey-lower { top: 584px; height: 21px; background: var(--steel-grey); }

  .brand {
    position: absolute;
    top: 137px;
    left: 0;
    width: 100%;
    height: 447px;
    display: flex;
    align-items: center;
    justify-content: center;
    gap: 18px;
  }
  .brand__dot {
    width: 62px;
    height: 62px;
    border-radius: 50%;
    background: var(--electric-blue);
    flex: none;
  }
  .brand__name {
    margin: 0;
    font-family: "PT Sans", Arial, sans-serif;
    font-weight: 700;
    font-size: 32px;
    letter-spacing: 0.5px;
    color: var(--electric-blue);
    white-space: nowrap;
  }

  .contact {
    position: absolute;
    left: 0;
    width: 100%;
    margin: 0;
    text-align: center;
    color: var(--text-light);
    text-shadow: 2px 3px 4px var(--text-shadow);
    line-height: 1;
  }
  .contact--name { top: 740px; font-size: 38px; letter-spacing: 1px; }
  .contact--phone-label { top: 840px; font-size: 37px; letter-spacing: 1px; left: 10px; }
  .contact--phone { top: 888px; font-size: 40px; letter-spacing: 1px; left: -6px; }
  .contact--email-label { top: 995px; font-family: "PT Serif", Georgia, serif; font-size: 39px; left: -28px; }
  .contact--email { top: 1044px; font-family: "PT Serif", Georgia, serif; font-size: 41px; }

  .icon {
    display: inline-block;
    vertical-align: middle;
    margin-right: 6px;
    filter: drop-shadow(2px 3px 3px var(--text-shadow));
  }
  .icon--phone { width: 30px; height: 36px; position: relative; top: -4px; }
  .icon--mail { width: 42px; height: 28px; margin-right: 14px; position: relative; top: -4px; }
</style>
</head>
<body>
  <main class="card">
    <div class="band band--top"></div>
    <div class="band band--grey-upper"></div>
    <div class="band band--brand"></div>
    <div class="band band--grey-lower"></div>

    <div class="brand">
      <span class="brand__dot"></span>
      <h1 class="brand__name">BRAVEN POWERLINE SERVICES</h1>
    </div>

    <p class="contact contact--name">Dalen Voskic EC40923</p>
    <p class="contact contact--phone-label">Phone Number:</p>
    <p class="contact contact--phone">
      <svg class="icon icon--phone" viewBox="0 0 24 30" aria-hidden="true">
        <path fill="#ffffff" d="M6 1c1-.6 2 0 2.6 1l2.6 5c.5 1 .2 2-.6 2.6l-2 1.4c-.4.3-.5.8-.3 1.3 1.2 3 2.6 5.6 4.4 8 .3.4.8.5 1.2.3l2.2-1.1c.9-.5 2-.2 2.6.6l3 4.6c.6 1 .3 2.1-.6 2.7l-2 1.3c-1.6 1-3.6 1-5.1-.2C8.4 24.7 3.6 16.8 2 8.6 1.7 6.8 2.5 5 4 3.9z"/>
      </svg>0417 358 942
    </p>
    <p class="contact contact--email-label">
      <svg class="icon icon--mail" viewBox="0 0 42 28" aria-hidden="true">
        <rect x="1" y="1" width="40" height="26" fill="#ffffff"/>
        <path d="M1 1 L21 16 L41 1" fill="none" stroke="#3a52a4" stroke-width="2.5"/>
        <path d="M1 27 L16 12 M41 27 L26 12" fill="none" stroke="#3a52a4" stroke-width="2"/>
      </svg>Email:
    </p>
    <p class="contact contact--email">dalen@bravenpowerline.com</p>
  </main>
</body>
</html>
```